Outdated Kelvoridge.com Website redesign

Kelvoridge.com is a construction supply company with 90% delivery of their product to local area builders. Phase one is about improving their online presence, mobile-friendly, and being informative. We are not looking to add any e-commerce abilities in this phase. Please review the documents attached for all the details you need to produce a mock-up. We are also redeveloping their logo (here in DC) but for now, use their old logo asa. place holder.

```html
<!DOCTYPE html>
<html lang="en">
<head>
<meta charset="utf-8">
<title>Kelvoridge Industries Co., Inc. — Construction Supplies</title>
<link href="https://fonts.googleapis.com/css2?family=Oswald:wght@500;600;700&family=Poppins:wght@400;500;600&display=swap" rel="stylesheet">
<style>
:root{
  --green:#0fb80f;
  --green-bright:#1ee01e;
  --green-dark:#078a07;
  --ink:#111111;
  --text:#555555;
  --muted:#8a8a8a;
  --light:#f3f3f3;
  --line:#e2e2e2;
  --frame:#d6d6d6;
  --white:#ffffff;
  --black:#000000;
  --star:#f5a623;
}
*{margin:0;padding:0;box-sizing:border-box}
html,body{width:1200px;height:3720px;overflow:hidden;background:var(--white)}
body{position:relative;font-family:'Poppins',sans-serif;color:var(--text)}
.abs{position:absolute}
.head{font-family:'Oswald',sans-serif;color:var(--ink);text-transform:uppercase;font-weight:700;letter-spacing:.2px}

/* top bar + header */
.topbar{left:570px;top:0;width:630px;height:35px;background:var(--black);clip-path:polygon(18px 0,100% 0,100% 100%,0 100%)}
.topbar .login{position:absolute;left:44px;top:9px;color:#fff;font:500 13px 'Oswald',sans-serif}
.topbar .soc{position:absolute;top:12px;width:11px;height:11px;border-radius:2px;background:#fff}
.brand{left:90px;top:40px;display:flex;align-items:center;gap:12px}
.brand .dot{width:52px;height:52px;border-radius:50%;background:var(--green)}
.brand .name{font:700 30px 'Oswald',sans-serif;color:var(--ink);letter-spacing:1px}
.nav{top:80px;font:500 14px 'Oswald',sans-serif;color:var(--ink);text-transform:uppercase}
.nav.active{color:var(--green)}
.search{left:783px;top:66px;width:232px;height:44px;border-radius:22px;background:var(--light)}
.search span{position:absolute;left:22px;top:13px;font-size:12px;color:var(--muted)}
.search i{position:absolute;right:8px;top:8px;width:28px;height:28px;border-radius:50%;background:var(--green)}

/* hero */
.hero-photo{left:0;top:140px;width:1200px;height:830px;background:linear-gradient(100deg,#2b2219 0%,#4a3a2c 45%,#6b5440 70%,#3a2e24 100%)}
.hero-title{left:88px;top:282px;font-size:88px;line-height:86px;color:#fff}
.hero-sub{left:88px;top:563px;font:500 18px/28px 'Oswald',sans-serif;color:#fff;text-transform:uppercase}
.btn{display:flex;align-items:center;justify-content:center;border-radius:24px;font:600 12px 'Poppins',sans-serif;text-transform:uppercase}
.btn-green{left:88px;top:640px;width:162px;height:42px;background:var(--green);color:#fff}
.mouse{left:91px;top:807px;width:18px;height:30px;border:2px solid #fff;border-radius:10px}
.mouse:after{content:"";position:absolute;left:6px;top:6px;width:2px;height:6px;background:#fff}
.slide-dot{left:1154px;width:3px;height:40px;background:#fff}

/* intro */
.photo-frame{left:169px;top:936px;width:293px;height:292px;background:var(--frame)}
.intro-photo{left:195px;top:963px;width:341px;height:443px;background:linear-gradient(160deg,#c9b49a,#8a6f55 60%,#5a4a3c);box-shadow:0 20px 40px rgba(0,0,0,.2)}
.play{left:490px;top:1138px;width:92px;height:92px;border-radius:50%;background:var(--green)}
.intro-title{left:627px;top:1012px;font-size:44px;line-height:46px}
.rule{width:44px;height:2px;background:var(--line)}
.intro-text{left:627px;top:1137px;width:430px;font-size:15px;line-height:26px}

/* why */
.band{left:0;top:1357px;width:1200px;height:751px;background:var(--light)}
.why-title{left:0;top:1498px;width:1200px;text-align:center;font-size:44px}
.feat{font:italic 600 14px 'Oswald',sans-serif;color:var(--ink);text-transform:uppercase;line-height:22px}
.feat.l{text-align:right}
.core-name{left:468px;top:1772px;width:280px;text-align:center;font:700 34px 'Oswald',sans-serif;color:#fff;letter-spacing:1px}

/* focus */
.focus-title{left:88px;top:2180px;font-size:44px}
.focus-text{left:88px;top:2251px;width:370px;font-size:15px;line-height:24px}
.arrow{top:2419px;width:52px;height:52px;border-radius:50%;background:#ececec;display:flex;align-items:center;justify-content:center;color:var(--ink);font-size:18px}
.card{top:2127px;height:386px}
.card span{position:absolute;left:0;bottom:18px;width:100%;text-align:center;font:700 27px 'Oswald',sans-serif;color:#fff;text-transform:uppercase}

/* testimonials */
.say-title{left:0;top:2596px;width:1200px;text-align:center;font-size:44px}
.tcard{top:2695px;width:274px}
.tcard .ava{position:absolute;left:12px;top:0;width:72px;height:72px;border-radius:50%;background:linear-gradient(#b89a86,#6b5648)}
.tcard .q{position:absolute;left:130px;top:6px;font:700 100px/1 'Oswald',sans-serif;color:#e4e4e4}
.tcard p{position:absolute;left:4px;top:90px;width:270px;font-size:12.5px;line-height:22px;color:#666}
.tcard .sep{position:absolute;left:0;top:170px;width:274px;height:1px;background:var(--line)}
.tcard .who{position:absolute;left:0;top:186px;font:600 15px 'Oswald',sans-serif;color:var(--ink);text-transform:uppercase}
.tcard .stars{position:absolute;right:0;top:186px;color:var(--star);font-size:14px;letter-spacing:1px}

/* footer */
.footer{left:0;top:2960px;width:1200px;height:760px;background:var(--black)}
.cta{left:156px;top:2992px;width:888px;height:192px;border-radius:96px;background:linear-gradient(90deg,var(--green-dark),var(--green) 50%,var(--green-bright))}
.cta-text{left:234px;top:3031px;font-size:47px;line-height:54px;color:#fff}
.btn-white{left:820px;top:3068px;width:163px;height:44px;background:#fff;color:var(--ink)}
.f-brand{left:120px;top:3380px;display:flex;align-items:center;gap:12px}
.f-brand .dot{width:52px;height:52px;border-radius:50%;background:var(--green)}
.f-brand .name{font:700 32px 'Oswald',sans-serif;color:#fff;letter-spacing:1px}
.f-soc{top:3485px;width:40px;height:40px;border-radius:50%;background:#222}
.f-h{top:3352px;font:600 17px 'Oswald',sans-serif;color:#fff;text-transform:uppercase}
.f-link{font-size:13px;color:#ddd}
.f-link:before{content:"›";margin-right:7px}
.f-info{font-size:13px;line-height:21px;color:#ddd;padding-left:26px}
.f-info i{position:absolute;left:0;top:4px;width:12px;height:12px;border-radius:50%;background:var(--green)}
.news-input{left:827px;top:3454px;width:259px;height:43px;border-radius:22px;background:#fff}
.news-input span{position:absolute;left:42px;top:13px;font-size:12px;color:#555}
.news-input i{position:absolute;right:0;top:0;width:43px;height:43px;border-radius:50%;background:var(--green)}
.f-rule{left:88px;top:3645px;width:1024px;height:1px;background:#2a2a2a}
.copy{left:0;top:3672px;width:1200px;text-align:center;font:500 13px 'Oswald',sans-serif;color:#fff;text-transform:uppercase}
.legal{top:3674px;font-size:12px;color:#ccc}
.to-top{left:1137px;top:3625px;width:42px;height:42px;border-radius:50%;background:var(--green)}
</style>
</head>
<body>

<!-- header -->
<div class="abs topbar">
  <span class="login">&#9679; LOGIN/SIGN UP</span>
  <span class="soc" style="left:381px"></span>
  <span class="soc" style="left:434px"></span>
  <span class="soc" style="left:485px"></span>
  <span class="soc" style="left:530px"></span>
</div>
<div class="abs brand"><span class="dot"></span><span class="name">KELVORIDGE</span></div>
<span class="abs nav active" style="left:322px">Home</span>
<span class="abs nav" style="left:378px">About us/our story</span>
<span class="abs nav" style="left:529px">Products &#709;</span>
<span class="abs nav" style="left:614px">Brands</span>
<span class="abs nav" style="left:684px">Contact us</span>
<div class="abs search"><span>Search products...</span><i></i></div>

<!-- hero -->
<div class="abs hero-photo" role="img" aria-label="Construction worker in a yellow hard hat and plaid shirt putting on a work glove on a job site"></div>
<div class="abs head hero-title">Kelvoridge<br>Industries<br>Co.,Inc.</div>
<div class="abs hero-sub">Construction supplies &amp; building materials<br>from our family to yours.</div>
<div class="abs btn btn-green">Contact us</div>
<div class="abs mouse"></div>
<div class="abs slide-dot" style="top:440px"></div>
<div class="abs slide-dot" style="top:492px;opacity:.6"></div>
<div class="abs slide-dot" style="top:543px"></div>

<svg class="abs" style="left:0;top:760px" width="1200" height="600" viewBox="0 0 1200 600">
  <path d="M0 200 C 250 40, 520 0, 820 40 C 1000 70, 1140 140, 1200 215 L1200 600 L0 600 Z" fill="#e6e6e6"/>
  <path d="M0 205 C 260 60, 520 30, 800 60 C 1000 90, 1150 170, 1200 240 L1200 600 L0 600 Z" fill="#fff"/>
  <line x1="822" y1="20" x2="822" y2="220" stroke="#0fb80f" stroke-width="1.5"/>
</svg>

<!-- intro -->
<div class="abs band"></div>
<div class="abs photo-frame"></div>
<div class="abs intro-photo" role="img" aria-label="Young worker in a hard hat carrying a stack of lumber on his shoulder"></div>
<div class="abs play"><svg width="92" height="92" viewBox="0 0 92 92"><path d="M39 34 L58 46 L39 58 Z" fill="#fff"/></svg></div>
<div class="abs head intro-title">When you need it now,<br>call Kelvoridge now!</div>
<div class="abs rule" style="left:627px;top:1115px"></div>
<p class="abs intro-text">Kelvoridge Industries Co., Inc. is a family owned and operated Wholesale Construction Supply Distributor serving the 5 boroughs of NY and northern NJ. Our knowledge, accuracy, and attention to detail will exceed your expectations with each of your construction and civil supply purchases.</p>

<!-- why -->
<div class="abs head why-title">Why do business with Kelvoridge?</div>
<div class="abs rule" style="left:578px;top:1562px"></div>

<svg class="abs" style="left:0;top:0" width="1200" height="2100" viewBox="0 0 1200 2100">
  <circle cx="608" cy="1790" r="183" fill="none" stroke="#0fb80f" stroke-width="2.5" stroke-dasharray="40 48"/>
  <circle cx="608" cy="1790" r="140" fill="#0fb80f"/>
  <g fill="#fff" stroke="#d9d9d9" stroke-width="1">
    <circle cx="513" cy="1627" r="29"/><circle cx="458" cy="1681" r="29"/><circle cx="427" cy="1750" r="29"/>
    <circle cx="426" cy="1825" r="29"/><circle cx="456" cy="1894" r="29"/><circle cx="514" cy="1949" r="29"/>
    <circle cx="608" cy="1974" r="29"/><circle cx="700" cy="1949" r="29"/><circle cx="758" cy="1894" r="29"/>
    <circle cx="788" cy="1825" r="29"/><circle cx="784" cy="1750" r="29"/><circle cx="752" cy="1681" r="29"/>
    <circle cx="700" cy="1627" r="29"/>
  </g>
  <g fill="none" stroke="#666" stroke-width="1.5" stroke-linecap="round">
    <path d="M503 1627 l6 -6 l6 6 l6 -6"/><circle cx="458" cy="1681" r="9"/><path d="M417 1745 h4 l3 10 h11 l2 -7 h-14"/>
    <path d="M418 1832 v-6 M424 1832 v-9 M430 1832 v-12 M436 1832 v-15"/><rect x="446" y="1888" width="14" height="10"/><circle cx="514" cy="1949" r="10"/>
    <path d="M598 1978 a10 10 0 0 1 20 0"/><path d="M692 1955 l14 -14"/><path d="M758 1886 a6 6 0 1 1 0.1 0 M758 1898 v6"/>
    <path d="M780 1818 h16 v10 l-8 6 l-8 -6 z"/><path d="M776 1758 l12 -14 l6 6 l-12 14 z"/><path d="M744 1681 a8 8 0 1 0 8 -8"/>
    <path d="M692 1620 h4 l4 12 h10"/>
  </g>
</svg>
<div class="abs core-name">KELVORIDGE</div>

<div class="abs feat l" style="right:735px;top:1612px">Service and relationship based company</div>
<div class="abs feat l" style="right:788px;top:1669px">Deliver fast and on time</div>
<div class="abs feat l" style="right:819px;top:1739px">One stop shop with wide range<br>of products</div>
<div class="abs feat l" style="right:822px;top:1820px">Knowledgeable sales associates</div>
<div class="abs feat l" style="right:783px;top:1910px">Piggy back unloading</div>
<div class="abs feat l" style="right:721px;top:1976px">Hours 6am - 5pm in NJ, 6am - 4pm LIC location</div>
<div class="abs feat" style="left:540px;top:2014px;width:130px;text-align:center">Union drivers</div>
<div class="abs feat" style="left:748px;top:1612px">Accurate shipments</div>
<div class="abs feat" style="left:801px;top:1669px">Minimal back orders</div>
<div class="abs feat" style="left:833px;top:1739px">Top name brands</div>
<div class="abs feat" style="left:835px;top:1820px">Reliable &amp; trustworthy</div>
<div class="abs feat" style="left:793px;top:1910px">Convenient locations</div>
<div class="abs feat" style="left:721px;top:1976px">Competitive pricing</div>

<!-- focus -->
<div class="abs head focus-title">We focus on</div>
<div class="abs rule" style="left:88px;top:2236px"></div>
<p class="abs focus-text">We focus on supplying construction materials for any size projects including but not limited to bridges, tunnels, highways, airports, water treatment plants &amp; more. With quick and reliable on time delivery, you'll have all the supplies you need to succeed.</p>
<div class="abs arrow" style="left:88px">&#8249;</div>
<div class="abs arrow" style="left:146px">&#8250;</div>
<div class="abs card" style="left:495px;width:282px;background:linear-gradient(180deg,#3f6f7d,#2a3b45 60%,#151c22)" role="img" aria-label="Arched steel bridge over water at dusk"><span>Bridges</span></div>
<div class="abs card" style="left:786px;width:280px;background:linear-gradient(180deg,#f0a640,#b86a2c 45%,#2c2a2e)" role="img" aria-label="Passenger airplane on the tarmac at sunset"><span>Airports</span></div>
<div class="abs card" style="left:1076px;width:124px;overflow:hidden;background:linear-gradient(180deg,#8aa0b0,#8a4b34 45%,#2e2a2a)" role="img" aria-label="Highway winding through red desert rock"><span style="text-align:left;left:82px;width:auto">Highways</span></div>

<!-- testimonials -->
<div class="abs head say-title">What our client say</div>
<div class="abs rule" style="left:578px;top:2660px"></div>

<div class="abs tcard" style="left:113px">
  <div class="ava" role="img" aria-label="Client portrait"></div><div class="q">&#8220;</div>
  <p>Aenean sollicitudin, lorem quis auctor consequat ipsum, nec sagittis sem nibh id elit duis sed odio sit amet nibh...</p>
  <div class="sep"></div><div class="who">Marisol Tenney</div><div class="stars">&#9733;&#9733;&#9733;&#9733;&#9733;</div>
</div>
<div class="abs tcard" style="left:459px">
  <div class="ava" role="img" aria-label="Client portrait"></div><div class="q">&#8220;</div>
  <p>Aenean sollicitudin, lorem quis auctor consequat ipsum, nec sagittis sem nibh id elit. Duis sed odio sit amet nibh...</p>
  <div class="sep"></div><div class="who">Deshawn Okafor</div><div class="stars">&#9733;&#9733;&#9733;&#9733;&#9733;</div>
</div>
<div class="abs tcard" style="left:806px">
  <div class="ava" role="img" aria-label="Client portrait"></div><div class="q">&#8220;</div>
  <p>Aenean sollicitudin, lorem quis auctor consequat ipsum, nec sagittis sem nibh id elit. Duis sed odio sit amet nibh...</p>
  <div class="sep"></div><div class="who">Rowan Keller</div><div class="stars">&#9733;&#9733;&#9733;&#9733;&#9733;</div>
</div>

<!-- footer -->
<div class="abs footer"></div>
<svg class="abs" style="left:0;top:2960px" width="1200" height="340" viewBox="0 0 1200 340">
  <path d="M0 0 L0 12 C 320 210, 780 300, 1200 322 L1200 0 Z" fill="#e3e3e3"/>
  <path d="M0 0 L0 4 C 330 190, 790 280, 1200 300 L1200 0 Z" fill="#fff"/>
</svg>
<div class="abs cta"></div>
<div class="abs head cta-text">Join now, for great offers<br>on our products!</div>
<div class="abs btn btn-white">Contact us</div>

<div class="abs f-brand"><span class="dot"></span><span class="name">KELVORIDGE</span></div>
<span class="abs f-soc" style="left:123px"></span>
<span class="abs f-soc" style="left:172px"></span>
<span class="abs f-soc" style="left:223px"></span>
<span class="abs f-soc" style="left:272px"></span>

<div class="abs f-h" style="left:381px">Quick links</div>
<div class="abs f-link" style="left:381px;top:3399px">Home</div>
<div class="abs f-link" style="left:381px;top:3431px">About us/our story</div>
<div class="abs f-link" style="left:381px;top:3462px">Products</div>
<div class="abs f-link" style="left:381px;top:3494px">Brands</div>
<div class="abs f-link" style="left:381px;top:3525px">Contact Us</div>

<div class="abs f-h" style="left:588px">Contact info</div>
<div class="abs f-info" style="left:588px;top:3397px"><i></i>Hours:<br>M-F 6am-6pm</div>
<div class="abs f-info" style="left:588px;top:3460px"><i></i>Phone:<br>201-555-0148</div>
<div class="abs f-info" style="left:588px;top:3522px"><i></i>Location:<br>480 Harlow Avenue<br>Fairbrook, NJ 07099</div>

<div class="abs f-h" style="left:826px">Newsletter</div>
<div class="abs" style="left:826px;top:3398px;font-size:13px;line-height:19px;color:#ddd">Subscribe to our email address to<br>get the latest news.</div>
<div class="abs news-input"><span>&#9993; Enter your email...</span><i></i></div>

<div class="abs f-rule"></div>
<div class="abs copy">&copy; Kelvoridge Industries Co., Inc. 2022 all rights reserved</div>
<div class="abs legal" style="left:885px">Terms &amp; Conditions</div>
<div class="abs legal" style="left:1027px">Privacy Policy</div>
<div class="abs to-top"><svg width="42" height="42" viewBox="0 0 42 42"><path d="M21 28 V15 M15 20 l6 -6 l6 6" fill="none" stroke="#fff" stroke-width="2"/></svg></div>

</body>
</html>
```